Packaging Design - Mailer Box for Canadian Gift Box Company

We are a new gift box company in Canada selling only Canadian products. We need a design for a mailer box that will be very unique and noticeable. We would like it to be very Canadian. It can be many colors.
I would like to close the mailer box with a sticker that could perhaps have our logo.
"Gifts from Canada's Best" to be included on the box.
We will be ordering at least 2 sizes so I'd like the artwork to be transferable to other box sizes
Updates
I will add a JPG file to my brief that I really love. I found it online but have not purchased it so do not have rights to use it.
Can anyone do something like this on the box design?
Industry/Entity Type
It Company
Colors
Designer to choose colors to be used in the design.
Look and feel
Each slider illustrates characteristics of the customer's brand and the style your logo design should communicate.

```html
<!DOCTYPE html>
<html lang="en">
<head>
<meta charset="utf-8">
<title>Hartley &amp; Pine — Briefcase Mailer Dieline</title>
<link rel="stylesheet" href="https://fonts.googleapis.com/css2?family=Cormorant+Garamond:wght@500&family=Inter:wght@400;700&display=swap">
<style>
  :root {
    --maple-red: #d62b27;
    --paper: #ffffff;
    --print-white: #f4f5f3;
    --cut: #4a4a4a;
    --crease: #f08a78;
    --hatch: #3b3b3b;
    --ink: #111111;
  }
  html, body {
    margin: 0;
    width: 1200px;
    height: 1200px;
    overflow: hidden;
    background: var(--paper);
  }
  .dieline { display: block; width: 1200px; height: 1200px; }
  .cut-edge { fill: var(--paper); stroke: var(--cut); stroke-width: 1.2; }
  .panel-red { fill: var(--maple-red); }
  .panel-white { fill: var(--print-white); }
  .tuck-flap { fill: url(#hatching); stroke: var(--cut); stroke-width: 1; }
  .slot { fill: url(#hatching); stroke: var(--cut); stroke-width: 1; }
  .slot-inner { fill: none; stroke: var(--cut); stroke-width: 1; }
  .crease-line { stroke: var(--crease); stroke-width: 0.8; fill: none; }
  .brand-name {
    font-family: "Cormorant Garamond", Georgia, serif;
    font-weight: 500;
    fill: var(--paper);
    text-anchor: middle;
  }
  .brand-name.on-white { fill: var(--maple-red); }
  .tagline {
    font-family: "Cormorant Garamond", Georgia, serif;
    font-weight: 500;
    fill: var(--paper);
    letter-spacing: 2.5px;
    text-anchor: middle;
  }
  .band-tagline {
    font-family: "Cormorant Garamond", Georgia, serif;
    font-weight: 500;
    font-size: 12.5px;
    fill: var(--paper);
    letter-spacing: 0.4px;
    text-anchor: middle;
  }
  .legend-title { font-family: "Inter", Arial, sans-serif; font-weight: 700; font-size: 17px; fill: var(--ink); }
  .legend-size { font-family: "Inter", Arial, sans-serif; font-size: 13px; fill: var(--ink); }
  .legend-label { font-family: "Inter", Arial, sans-serif; font-size: 9.5px; fill: var(--ink); }
  .legend-note { font-family: "Inter", Arial, sans-serif; font-size: 7px; font-style: italic; fill: var(--ink); }
</style>
</head>
<body>
<svg class="dieline" viewBox="0 0 1300 1300" xmlns="http://www.w3.org/2000/svg" role="img" aria-label="Flat dieline of the Hartley and Pine briefcase mailer box">
  <defs>
    <pattern id="hatching" width="9" height="9" patternUnits="userSpaceOnUse" patternTransform="rotate(45)">
      <rect width="9" height="9" fill="#ffffff"/>
      <line x1="0" y1="0" x2="0" y2="9" stroke="var(--hatch)" stroke-width="1"/>
    </pattern>
  </defs>

  <g class="cut-outline">
    <rect class="cut-edge" x="408" y="48" width="484" height="150"/>
    <path class="cut-edge" d="M94 198 H250 V572 H94 V525 H88 V460 H94 V335 H88 V280 H94 Z"/>
    <path class="cut-edge" d="M1206 198 H1050 V572 H1206 V525 H1212 V460 H1206 V335 H1212 V280 H1206 Z"/>
    <rect class="cut-edge" x="250" y="195" width="800" height="380"/>
    <rect class="cut-edge" x="408" y="572" width="484" height="150"/>
    <path class="cut-edge" d="M405 730 L282 744 Q266 746 266 762 V1040 Q266 1060 300 1070 L408 1098 H892 L1000 1070 Q1034 1060 1034 1040 V762 Q1034 746 1018 744 L895 730 Z"/>
    <path class="cut-edge" d="M405 1104 H294 Q276 1104 276 1122 V1150 Q276 1250 380 1250 H920 Q1024 1250 1024 1150 V1122 Q1024 1104 1006 1104 H895 Z"/>
  </g>

  <path class="tuck-flap" d="M222 48 H408 V185 L394 192 H262 L250 182 H222 Z"/>
  <path class="tuck-flap" d="M1078 48 H892 V185 L906 192 H1038 L1050 182 H1078 Z"/>
  <path class="tuck-flap" d="M222 718 H408 V583 L394 576 H262 L250 586 H222 Z"/>
  <path class="tuck-flap" d="M1078 718 H892 V583 L906 576 H1038 L1050 586 H1078 Z"/>

  <rect class="panel-red" x="418" y="58" width="464" height="134"/>
  <rect class="panel-red" x="104" y="207" width="136" height="355"/>
  <rect class="panel-red" x="252" y="203" width="262" height="367"/>
  <rect class="panel-white" x="514" y="196" width="272" height="376"/>
  <rect class="panel-red" x="786" y="203" width="262" height="367"/>
  <rect class="panel-red" x="1060" y="207" width="136" height="355"/>
  <rect class="panel-red" x="418" y="578" width="464" height="140"/>
  <path class="panel-red" d="M418 735 L290 752 Q276 754 276 768 V1036 Q276 1052 304 1060 L418 1090 H882 L996 1060 Q1024 1052 1024 1036 V768 Q1024 754 1010 752 L882 735 Z"/>
  <path class="panel-red" d="M300 1112 H1000 Q1016 1112 1016 1128 V1148 Q1016 1240 924 1240 H376 Q284 1240 284 1148 V1128 Q284 1112 300 1112 Z"/>

  <g class="slots">
    <rect class="slot" x="392" y="262" width="33" height="71"/><rect class="slot-inner" x="401" y="272" width="15" height="51"/>
    <rect class="slot" x="392" y="435" width="33" height="72"/><rect class="slot-inner" x="401" y="445" width="15" height="52"/>
    <rect class="slot" x="876" y="262" width="33" height="71"/><rect class="slot-inner" x="885" y="272" width="15" height="51"/>
    <rect class="slot" x="876" y="435" width="33" height="72"/><rect class="slot-inner" x="885" y="445" width="15" height="52"/>
  </g>

  <g class="creases">
    <line class="crease-line" x1="408" y1="195" x2="892" y2="195"/>
    <line class="crease-line" x1="250" y1="203" x2="250" y2="570"/>
    <line class="crease-line" x1="402" y1="203" x2="402" y2="570"/>
    <line class="crease-line" x1="514" y1="196" x2="514" y2="572"/>
    <line class="crease-line" x1="786" y1="196" x2="786" y2="572"/>
    <line class="crease-line" x1="898" y1="203" x2="898" y2="570"/>
    <line class="crease-line" x1="1050" y1="203" x2="1050" y2="570"/>
    <line class="crease-line" x1="408" y1="574" x2="892" y2="574"/>
    <line class="crease-line" x1="408" y1="720" x2="892" y2="720"/>
    <line class="crease-line" x1="418" y1="735" x2="418" y2="1100"/>
    <line class="crease-line" x1="882" y1="735" x2="882" y2="1100"/>
    <line class="crease-line" x1="408" y1="1102" x2="892" y2="1102"/>
    <line class="crease-line" x1="406" y1="1112" x2="406" y2="1240"/>
    <line class="crease-line" x1="894" y1="1112" x2="894" y2="1240"/>
  </g>

  <!-- Top lid panel (upside down) -->
  <g transform="rotate(180 650 125)">
    <text class="tagline" x="784" y="128" font-size="8">GIVE CANADA'S BEST</text>
    <text class="brand-name" x="510" y="132" font-size="24">Hartley &amp; Pine</text>
  </g>

  <!-- Left side panel -->
  <g transform="rotate(90 330 290)">
    <text class="brand-name" x="330" y="298" font-size="24">Hartley &amp; Pine</text>
  </g>
  <g transform="rotate(90 325 485)">
    <text class="tagline" x="325" y="488" font-size="8">GIVE CANADA'S BEST</text>
  </g>

  <!-- Front inner panel -->
  <text class="brand-name on-white" x="652" y="505" font-size="32">Hartley &amp; Pine</text>
  <rect class="panel-red" x="573" y="537" width="160" height="35"/>
  <text class="band-tagline" x="653" y="559">GIVE CANADA'S BEST</text>

  <!-- Right side panel -->
  <g transform="rotate(-90 985 292)">
    <text class="tagline" x="985" y="295" font-size="8">GIVE CANADA'S BEST</text>
  </g>
  <g transform="rotate(-90 975 485)">
    <text class="brand-name" x="975" y="493" font-size="24">Hartley &amp; Pine</text>
  </g>

  <!-- Back panel -->
  <text class="brand-name" x="510" y="655" font-size="25">Hartley &amp; Pine</text>
  <text class="tagline" x="786" y="653" font-size="8">GIVE CANADA'S BEST</text>

  <!-- Main lid -->
  <text class="brand-name" x="652" y="925" font-size="34">Hartley &amp; Pine</text>

  <g class="legend">
    <text class="legend-title" x="122" y="1072">Briefcase Mailer</text>
    <text class="legend-size" x="122" y="1089">12.5″ x 10″ x 4″</text>
    <line x1="122" y1="1115" x2="143" y2="1115" stroke="var(--crease)" stroke-width="1.2"/>
    <text class="legend-label" x="149" y="1119">Crease Line</text>
    <line x1="122" y1="1135" x2="143" y2="1135" stroke="var(--ink)" stroke-width="1.5"/>
    <text class="legend-label" x="149" y="1139">Cut Line</text>
    <rect x="122" y="1148" width="21" height="14" fill="#e4e4e4"/>
    <text class="legend-label" x="149" y="1158">Printable Area</text>
    <text class="legend-note" x="149" y="1168">*Ensure design stays in</text>
    <text class="legend-note" x="149" y="1177">the safe area</text>
    <rect x="122" y="1189" width="21" height="12" fill="url(#hatching)" stroke="var(--cut)" stroke-width="0.8"/>
    <text class="legend-label" x="149" y="1198">Tucked-in Flaps</text>
    <text class="legend-note" x="149" y="1208">*These flaps will be hidden</text>
    <text class="legend-note" x="149" y="1217">after the box is made</text>
  </g>
</svg>
</body>
</html>
```